PowerPoint template for training in Early-Roots Counseling

We just had a logo designed using artbazaarly, and we need a PowerPoint template for our treatment model.
Early-Roots Counseling (ERC), an intervention model for children under age 6 who have experienced one or more traumatic events (accidents, medical procedures, abuse, witnessing violence). We are a non-profit organization spreading this treatment around the country by training mental health professionals. We have 55 ERC trainers, and we would like all of them to use the same PowerPoint template.

Core themes of our work include: safety, connection, attachment, growth, strength, and resilience.

We would like the designs to include the logo and to use the color green. Other colors and other greens can be used as well. We often train for 4 days straight, so it is important that the PowerPoint template be pleasing to look at and convey a sense of peace, calm, and even a little fun rather than being overly stiff and business like.

Looking forward to seeing the designs. If we find a design we love, we may end the contest early.

Reason: I just made this project guaranteed as I have at least one design I am considering. I will need to take it to a vote with my colleagues, so I am extending the deadline. If you send a good design in soon, we will include it in the vote. We may end this project early as soon as our vote is completed. Thank you all for submitting.

Industry/Entity Type

Training

Font styles to use
Sans Serif

Requirements
Must have
• Please include the logo
• Deliverables include:
• 1) Title slide
• 2) Title and content (presentation body slide) - I believe we prefer a white background for the middle area
• 3) Section header slide
• 4) Closing slide
• 5) Photoshop (PSD) files for all graphic elements.
• 6) Font files for all fonts used.
• We may also request additional slide formats once the design is selected (e.g. two content and comparison slides)
Nice to have
• Some color (green)in the slide design in addition to the logo.
• Please show us what this will look like using the PowerPoint slides we uploaded.
Should not have
• In general, we would not use red.
• Not just a wihite background with the logo on the corner.

```html
<!DOCTYPE html>
<html lang="en">
<head>
<meta charset="utf-8">
<title>Early-Roots Counseling — Presentation Template</title>
<link rel="stylesheet" href="https://fonts.googleapis.com/css2?family=Open+Sans:wght@400;600;700;800&display=swap">
<style>
  :root{
    --green:#7ab642;
    --green-dark:#4e8a2a;
    --green-light:#a8d47a;
    --green-pale:#eaf4df;
    --blue:#2f6db5;
    --orange:#f39a1e;
    --ink:#4a4a4a;
    --muted:#9a9a9a;
    --rule:#d9d9d9;
    --paper:#ffffff;
    --canvas:#ffffff;
  }
  *{box-sizing:border-box;margin:0;padding:0}
  html,body{width:835px;height:1200px;overflow:hidden;background:var(--canvas)}
  body{font-family:"Open Sans",Arial,sans-serif;color:var(--ink)}
  .deck{
    display:grid;
    grid-template-columns:repeat(3,263px);
    grid-template-rows:repeat(7,160px);
    column-gap:11px;row-gap:10px;
    padding:5px 10px;
  }
  .slide{position:relative;overflow:hidden;background:var(--paper);box-shadow:0 0 0 1px #e4e4e4}
  .photo{position:absolute}
  /* body slide frame */
  .slide-title{position:absolute;left:12px;top:9px;font-size:9px;font-weight:800;color:var(--green);letter-spacing:.3px;text-transform:uppercase}
  .title-rule{position:absolute;left:12px;right:12px;top:24px;height:1px;background:var(--green)}
  .footer{position:absolute;left:0;right:0;bottom:0;height:12px;border-top:1px solid var(--rule);display:flex;align-items:center;justify-content:space-between;padding:0 12px}
  .footer-brand{font-size:4.5px;font-weight:700;color:var(--green)}
  .footer-page{font-size:4.5px;color:var(--muted)}
  .brand{display:flex;align-items:center;gap:5px}
  .brand-dot{border-radius:50%;background:var(--green)}
  .brand-name{font-weight:800;color:var(--green)}
  .line{height:2px;background:#d4d4d4;margin-bottom:3px;border-radius:1px}
  .small{font-size:4.5px;line-height:1.45;color:var(--muted)}
  .bold-small{font-size:5px;font-weight:700;color:var(--ink)}
  /* section slides */
  .section{color:#fff}
  .section-mark{position:absolute;width:26px;height:26px;border-radius:50%;border:2px solid rgba(255,255,255,.85)}
  .section-title{position:absolute;font-size:9px;font-weight:700}
  .section-sub{position:absolute;font-size:4.5px;opacity:.85}
  /* agenda */
  .agenda{background:var(--green)}
  .agenda-tag{position:absolute;right:10px;top:8px;background:var(--green-dark);color:#fff;font-size:6px;font-weight:700;padding:2px 8px}
  .agenda-panel{position:absolute;left:0;top:0;bottom:0;width:70px;background:var(--green-light)}
  .agenda-list{position:absolute;left:80px;right:10px;top:28px;display:grid;grid-template-columns:1fr 1fr;gap:8px 8px}
  .agenda-item{display:flex;gap:4px;align-items:flex-start;color:#fff}
  .agenda-num{width:12px;height:12px;background:#fff;color:var(--green);font-size:6px;font-weight:800;display:flex;align-items:center;justify-content:center;flex:none}
  .agenda-item b{display:block;font-size:5.5px}
  .agenda-item span{font-size:4px;opacity:.85}
  table{border-collapse:collapse;width:100%}
  td,th{font-size:4.5px;padding:2px 4px;text-align:left}
  th{background:var(--green);color:#fff}
  tr:nth-child(even) td{background:var(--green-pale)}
</style>
</head>
<body>
<main class="deck">

  <!-- 1 cover with photo -->
  <section class="slide">
    <div class="photo" role="img" aria-label="Photo of a parent and young children at a kitchen table" style="inset:0 0 38px 0;background:linear-gradient(135deg,#c9a27a,#e8d6b9 50%,#8d9c6a)"></div>
    <div style="position:absolute;left:0;right:0;bottom:0;height:38px;background:var(--green);padding:7px 12px;color:#fff">
      <div style="font-size:7px;font-weight:700">Early-Roots Counseling</div>
      <div style="font-size:4.5px;opacity:.9;margin-top:2px">Training for mental health professionals</div>
    </div>
  </section>

  <!-- 2 title slide -->
  <section class="slide">
    <div class="brand" style="position:absolute;left:0;right:0;top:24px;justify-content:center">
      <span class="brand-dot" style="width:14px;height:14px"></span>
      <span class="brand-name" style="font-size:12px">Early-Roots Counseling</span>
    </div>
    <div style="position:absolute;left:30px;right:30px;top:62px;text-align:center">
      <div style="font-size:7px;font-weight:700;color:var(--ink);line-height:1.35">Using Early-Roots Counseling to Heal Young Children Exposed to Trauma</div>
      <div class="small" style="margin-top:5px">Presenter name · Training date</div>
    </div>
    <div style="position:absolute;left:0;right:0;bottom:0;height:10px;background:var(--green)"></div>
  </section>

  <!-- 3 agenda -->
  <section class="slide agenda">
    <div class="agenda-panel"></div>
    <div class="agenda-tag">AGENDA</div>
    <div class="agenda-list">
      <div class="agenda-item"><div class="agenda-num">1</div><div><b>Section 1</b><span>Safety and trust first</span></div></div>
      <div class="agenda-item"><div class="agenda-num">4</div><div><b>Section 4</b><span>Growth through play</span></div></div>
      <div class="agenda-item"><div class="agenda-num">2</div><div><b>Section 2</b><span>Building connection</span></div></div>
      <div class="agenda-item"><div class="agenda-num">5</div><div><b>Section 5</b><span>Family strengths</span></div></div>
      <div class="agenda-item"><div class="agenda-num">3</div><div><b>Section 3</b><span>Secure attachment</span></div></div>
      <div class="agenda-item"><div class="agenda-num">6</div><div><b>Section 6</b><span>Lasting resilience</span></div></div>
    </div>
  </section>

  <!-- 4 team -->
  <section class="slide">
    <div class="slide-title">The Team</div><div class="title-rule"></div>
    <div style="position:absolute;left:12px;top:42px;width:72px;height:80px;background:#eeeeee"></div>
    <div style="position:absolute;left:92px;top:42px;width:80px;height:80px;background:var(--green);padding:8px;color:#fff">
      <div style="font-size:6px;font-weight:700">Team Member</div>
      <div style="font-size:4.5px;opacity:.9;margin-top:3px;line-height:1.4">Lead trainer with many years of work in early childhood care.</div>
    </div>
    <div style="position:absolute;left:180px;top:42px;width:71px;height:80px;background:#eeeeee"></div>
    <footer class="footer"><span class="footer-brand">Early-Roots Counseling</span><span class="footer-page">4</span></footer>
  </section>

  <!-- 5 image slide with icon -->
  <section class="slide">
    <div class="slide-title">Image Slide With Icon</div><div class="title-rule"></div>
    <div class="photo" role="img" aria-label="Photo of a mother holding her young child" style="left:12px;right:12px;top:30px;height:58px;background:linear-gradient(120deg,#9fb7d4,#e6d2bd 60%,#b98e6e)"></div>
    <div style="position:absolute;left:12px;right:12px;top:94px;display:flex;justify-content:space-around">
      <svg width="22" height="22" viewBox="0 0 22 22"><circle cx="11" cy="11" r="11" fill="#7ab642"/><path d="M6 11l3 3 7-7" stroke="#fff" stroke-width="2" fill="none"/></svg>
      <svg width="22" height="22" viewBox="0 0 22 22"><circle cx="11" cy="11" r="11" fill="#2f6db5"/><path d="M11 5a4 4 0 0 1 4 4c0 3-4 8-4 8s-4-5-4-8a4 4 0 0 1 4-4z" fill="#fff"/></svg>
      <svg width="22" height="22" viewBox="0 0 22 22"><circle cx="11" cy="11" r="11" fill="#f39a1e"/><path d="M6 11h9M12 7l4 4-4 4" stroke="#fff" stroke-width="2" fill="none"/></svg>
    </div>
    <div style="position:absolute;left:12px;right:12px;top:121px;display:flex;justify-content:space-around;text-align:center">
      <div class="small" style="width:60px">Safety comes first</div>
      <div class="small" style="width:60px">Close connection</div>
      <div class="small" style="width:60px">Steady growth</div>
    </div>
    <footer class="footer"><span class="footer-brand">Early-Roots Counseling</span><span class="footer-page">5</span></footer>
  </section>

  <!-- 6 line format -->
  <section class="slide">
    <div class="slide-title">Line Format</div><div class="title-rule"></div>
    <svg style="position:absolute;left:12px;top:34px" width="150" height="100" viewBox="0 0 150 100">
      <g stroke="#e4e4e4" stroke-width=".6"><line x1="10" y1="10" x2="150" y2="10"/><line x1="10" y1="35" x2="150" y2="35"/><line x1="10" y1="60" x2="150" y2="60"/><line x1="10" y1="85" x2="150" y2="85"/></g>
      <polyline points="12,70 40,55 68,62 96,35 124,40 148,18" fill="none" stroke="#7ab642" stroke-width="2"/>
      <polyline points="12,80 40,72 68,50 96,58 124,30 148,34" fill="none" stroke="#2f6db5" stroke-width="2"/>
      <polyline points="12,60 40,78 68,74 96,66 124,60 148,50" fill="none" stroke="#f39a1e" stroke-width="2"/>
    </svg>
    <div style="position:absolute;left:172px;right:12px;top:40px">
      <div class="bold-small" style="margin-bottom:4px">Progress</div>
      <div class="small">Session scores rise as families build trust and routine over time.</div>
    </div>
    <footer class="footer"><span class="footer-brand">Early-Roots Counseling</span><span class="footer-page">6</span></footer>
  </section>

  <!-- 7 testimonials -->
  <section class="slide">
    <div class="slide-title">Testimonials</div><div class="title-rule"></div>
    <div class="photo" role="img" aria-label="Portrait photo of a trainer" style="left:12px;top:38px;width:26px;height:26px;background:linear-gradient(#b9c6d6,#8a9bb0)"></div>
    <div style="position:absolute;left:44px;right:12px;top:38px"><div class="small">"The training changed how I listen to the youngest children in my care."</div><div class="bold-small" style="margin-top:2px">Trainer Name</div></div>
    <div class="photo" role="img" aria-label="Portrait photo of a clinician" style="left:12px;top:84px;width:26px;height:26px;background:linear-gradient(#d6c3b0,#a88d74)"></div>
    <div style="position:absolute;left:44px;right:12px;top:84px"><div class="small">"Calm, clear and practical. Our whole team now uses the model daily."</div><div class="bold-small" style="margin-top:2px">Clinician Name</div></div>
    <footer class="footer"><span class="footer-brand">Early-Roots Counseling</span><span class="footer-page">7</span></footer>
  </section>

  <!-- 8 bullet list -->
  <section class="slide">
    <div class="slide-title">Bullet List</div><div class="title-rule"></div>
    <ul style="position:absolute;left:20px;right:14px;top:34px;list-style:none">
      <li class="small" style="margin-bottom:5px"><span style="color:var(--green)">■</span> Children under six can heal with the right support around them.</li>
      <li class="small" style="margin-bottom:5px"><span style="color:var(--green)">■</span> Caregivers are partners in every step of treatment.</li>
      <li class="small" style="margin-bottom:5px"><span style="color:var(--green)">■</span> Play helps a child share what words cannot yet say.</li>
      <li class="small" style="margin-bottom:5px"><span style="color:var(--green)">■</span> Safe routines rebuild trust after a hard event.</li>
      <li class="small"><span style="color:var(--green)">■</span> Strength and resilience grow inside close bonds.</li>
    </ul>
    <footer class="footer"><span class="footer-brand">Early-Roots Counseling</span><span class="footer-page">8</span></footer>
  </section>

  <!-- 9 section with blue panel -->
  <section class="slide section">
    <div class="photo" role="img" aria-label="Photo of a parent embracing a smiling child" style="left:0;top:0;bottom:0;width:165px;background:linear-gradient(135deg,#f0dcc8,#d9b296 55%,#a8b6c6)"></div>
    <div style="position:absolute;left:165px;right:0;top:0;bottom:0;background:var(--blue)"></div>
    <div class="section-mark" style="left:201px;top:40px"></div>
    <div class="section-title" style="left:176px;top:76px">Section Title</div>
    <div class="section-sub" style="left:176px;top:90px">Short subtitle here</div>
  </section>

  <!-- 10 chart slide donut -->
  <section class="slide">
    <div class="slide-title">Chart Slide</div><div class="title-rule"></div>
    <svg style="position:absolute;left:101px;top:38px" width="60" height="60" viewBox="0 0 60 60">
      <circle cx="30" cy="30" r="22" fill="none" stroke="#7ab642" stroke-width="10" stroke-dasharray="62 138.2" transform="rotate(-90 30 30)"/>
      <circle cx="30" cy="30" r="22" fill="none" stroke="#2f6db5" stroke-width="10" stroke-dasharray="42 138.2" stroke-dashoffset="-62" transform="rotate(-90 30 30)"/>
      <circle cx="30" cy="30" r="22" fill="none" stroke="#f39a1e" stroke-width="10" stroke-dasharray="34.2 138.2" stroke-dashoffset="-104" transform="rotate(-90 30 30)"/>
    </svg>
    <div style="position:absolute;left:12px;top:44px;width:80px;text-align:right"><div class="bold-small" style="color:var(--green)">45%</div><div class="small">Home visits</div><div class="bold-small" style="color:var(--blue);margin-top:6px">30%</div><div class="small">Clinic sessions</div></div>
    <div style="position:absolute;left:170px;top:44px;width:80px"><div class="bold-small" style="color:var(--orange)">25%</div><div class="small">Group training</div></div>
    <div class="small" style="position:absolute;left:12px;right:12px;top:110px;text-align:center">Share of service time across the program year.</div>
    <footer class="footer"><span class="footer-brand">Early-Roots Counseling</span><span class="footer-page">10</span></footer>
  </section>

  <!-- 11 section with green band over photo -->
  <section class="slide section">
    <div class="photo" role="img" aria-label="Photo of hands forming a heart against a sunset" style="inset:0;background:linear-gradient(180deg,#f4b860,#e07b2e 60%,#5a3a22)"></div>
    <div style="position:absolute;left:0;right:0;top:88px;height:40px;background:rgba(122,182,66,.9)"></div>
    <div class="section-title" style="left:14px;top:96px">Section Title</div>
    <div class="section-sub" style="left:14px;top:110px">Short subtitle here</div>
  </section>

  <!-- 12 chart slide three donuts -->
  <section class="slide">
    <div class="slide-title">Chart Slide</div><div class="title-rule"></div>
    <div style="position:absolute;left:12px;right:12px;top:40px;display:flex;justify-content:space-around;text-align:center">
      <div><svg width="44" height="44" viewBox="0 0 44 44"><circle cx="22" cy="22" r="17" fill="none" stroke="#eeeeee" stroke-width="6"/><circle cx="22" cy="22" r="17" fill="none" stroke="#7ab642" stroke-width="6" stroke-dasharray="80 107" transform="rotate(-90 22 22)"/><text x="22" y="25" font-size="8" font-weight="700" text-anchor="middle" fill="#4a4a4a">75%</text></svg><div class="small" style="width:60px">Safety gained</div></div>
      <div><svg width="44" height="44" viewBox="0 0 44 44"><circle cx="22" cy="22" r="17" fill="none" stroke="#eeeeee" stroke-width="6"/><circle cx="22" cy="22" r="17" fill="none" stroke="#2f6db5" stroke-width="6" stroke-dasharray="64 107" transform="rotate(-90 22 22)"/><text x="22" y="25" font-size="8" font-weight="700" text-anchor="middle" fill="#4a4a4a">60%</text></svg><div class="small" style="width:60px">Bonds improved</div></div>
      <div><svg width="44" height="44" viewBox="0 0 44 44"><circle cx="22" cy="22" r="17" fill="none" stroke="#eeeeee" stroke-width="6"/><circle cx="22" cy="22" r="17" fill="none" stroke="#f39a1e" stroke-width="6" stroke-dasharray="96 107" transform="rotate(-90 22 22)"/><text x="22" y="25" font-size="8" font-weight="700" text-anchor="middle" fill="#4a4a4a">90%</text></svg><div class="small" style="width:60px">Families engaged</div></div>
    </div>
    <footer class="footer"><span class="footer-brand">Early-Roots Counseling</span><span class="footer-page">12</span></footer>
  </section>

  <!-- 13 section with orange panel over photo -->
  <section class="slide section">
    <div class="photo" role="img" aria-label="Photo of a smiling family group" style="inset:0;background:linear-gradient(135deg,#a6b894,#d8c0a4 50%,#8c6f58)"></div>
    <div style="position:absolute;left:0;top:70px;width:120px;height:50px;background:rgba(243,154,30,.92)"></div>
    <div class="section-title" style="left:12px;top:80px">Section Title</div>
    <div class="section-sub" style="left:12px;top:94px">Short subtitle here</div>
  </section>

  <!-- 14 two column image -->
  <section class="slide">
    <div class="slide-title">Two Column Image</div><div class="title-rule"></div>
    <div class="photo" role="img" aria-label="Photo of a child playing with a caregiver" style="left:12px;top:32px;width:114px;height:58px;background:linear-gradient(135deg,#c2d4a4,#e3cdb4)"></div>
    <div class="photo" role="img" aria-label="Photo of a parent reading with a toddler" style="left:137px;top:32px;width:114px;height:58px;background:linear-gradient(135deg,#b4c8dc,#dcc0a6)"></div>
    <div style="position:absolute;left:12px;top:96px;width:114px"><div class="bold-small">Column one</div><div class="small">Playful time builds a warm and steady bond.</div></div>
    <div style="position:absolute;left:137px;top:96px;width:114px"><div class="bold-small">Column two</div><div class="small">Shared stories help a child feel safe again.</div></div>
    <footer class="footer"><span class="footer-brand">Early-Roots Counseling</span><span class="footer-page">14</span></footer>
  </section>

  <!-- 15 blue section -->
  <section class="slide section" style="background:var(--blue)">
    <div class="section-mark" style="left:14px;top:60px"></div>
    <div class="section-title" style="left:14px;top:94px">Section Title</div>
    <div class="section-sub" style="left:14px;top:108px">Short subtitle here</div>
  </section>

  <!-- 16 table -->
  <section class="slide">
    <div class="slide-title">Table Format</div><div class="title-rule"></div>
    <div style="position:absolute;left:12px;right:12px;top:34px">
      <table>
        <tr><th>Module</th><th>Day</th><th>Hours</th><th>Focus</th></tr>
        <tr><td>Intro</td><td>1</td><td>6</td><td>Safety</td></tr>
        <tr><td>Module A</td><td>2</td><td>6</td><td>Connection</td></tr>
        <tr><td>Module B</td><td>3</td><td>6</td><td>Attachment</td></tr>
        <tr><td>Module C</td><td>4</td><td>5</td><td>Resilience</td></tr>
      </table>
    </div>
    <footer class="footer"><span class="footer-brand">Early-Roots Counseling</span><span class="footer-page">16</span></footer>
  </section>

  <!-- 17 green section -->
  <section class="slide section" style="background:var(--green)">
    <div class="section-mark" style="left:14px;top:60px"></div>
    <div class="section-title" style="left:14px;top:94px">Section Title</div>
    <div class="section-sub" style="left:14px;top:108px">Short subtitle here</div>
  </section>

  <!-- 18 single image -->
  <section class="slide">
    <div class="slide-title">Single Image Slide</div><div class="title-rule"></div>
    <div class="photo" role="img" aria-label="Photo of a mother and child smiling together" style="left:12px;top:32px;width:130px;height:98px;background:linear-gradient(135deg,#e6d0b8,#b89478 60%,#9fb18a)"></div>
    <div style="position:absolute;left:152px;right:12px;top:36px">
      <div class="bold-small" style="margin-bottom:4px">Image title</div>
      <div class="small">Caring adults give young children the calm base they need to grow and recover.</div>
    </div>
    <footer class="footer"><span class="footer-brand">Early-Roots Counseling</span><span class="footer-page">18</span></footer>
  </section>

  <!-- 19 orange section -->
  <section class="slide section" style="background:var(--orange)">
    <div class="section-mark" style="left:14px;top:60px"></div>
    <div class="section-title" style="left:14px;top:94px">Section Title</div>
    <div class="section-sub" style="left:14px;top:108px">Short subtitle here</div>
  </section>

  <!-- 20 two column text -->
  <section class="slide">
    <div class="slide-title">Two Column Text</div><div class="title-rule"></div>
    <div style="position:absolute;left:12px;top:36px;width:112px"><div class="bold-small" style="color:var(--green);margin-bottom:3px">First topic</div><div class="small">Trauma in early years shapes how a child sees the world. Gentle care helps reshape it.</div></div>
    <div style="position:absolute;left:139px;top:36px;width:112px"><div class="bold-small" style="color:var(--green);margin-bottom:3px">Second topic</div><div class="small">Trainers guide clinicians to work with the whole family in a calm, hopeful way.</div></div>
    <footer class="footer"><span class="footer-brand">Early-Roots Counseling</span><span class="footer-page">20</span></footer>
  </section>

  <!-- 21 closing -->
  <section class="slide section">
    <div class="photo" role="img" aria-label="Photo of a family relaxing together outdoors" style="inset:0;background:linear-gradient(135deg,#cdb89c,#a7c08a 55%,#6f8c55)"></div>
    <div style="position:absolute;left:0;top:0;bottom:0;width:105px;background:rgba(122,182,66,.92)"></div>
    <div style="position:absolute;left:12px;top:40px;font-size:12px;font-weight:800;line-height:1.1">THANK<br>YOU</div>
    <div class="section-sub" style="left:12px;top:72px">Questions and discussion</div>
    <div class="brand" style="position:absolute;left:12px;bottom:14px">
      <span class="brand-dot" style="width:7px;height:7px;background:#fff"></span>
      <span class="brand-name" style="font-size:6px;color:#fff">Early-Roots Counseling</span>
    </div>
  </section>

</main>
</body>
</html>
```